CV Template

We need a graphic design to our new CV templates for our consultants. We are a small young Danish upcoming IT-business company making software solutions for our customers etc. You can visit our new website here: dev.solbakken-data.com, then you can see our web design, colors etc. I have attached a file for your inspiration :-) In the presentation I would like to have a picture of the employee, some text who descripe the profile/consultant and then I imagine that there is a table where we can write the employee's skills etc.

I would like the design to be "fresh & catchy" :-)

Looking forward to hear from you.

Best regards,
Birgit

```html
<!DOCTYPE html>
<html lang="da">
<head>
<meta charset="utf-8">
<title>CV – Solbakken Data</title>
<link rel="stylesheet" href="https://fonts.googleapis.com/css2?family=Oswald:wght@400;500&family=Open+Sans:wght@300;400&display=swap">
<style>
  :root {
    --stage: #e6e9ec;
    --paper: #ffffff;
    --side: #ececec;
    --teal: #2a8393;
    --teal-dark: #2b6672;
    --table-light: #a9d6e2;
    --table-pale: #d8edf3;
    --skills-band: #c6d0d7;
    --skill-line: #f3f6f8;
    --footer: #8fa2ae;
    --ink: #3a3a3a;
  }
  * { box-sizing: border-box; margin: 0; padding: 0; }
  html, body { width: 1200px; height: 675px; overflow: hidden; background: var(--stage); }
  body { display: flex; justify-content: center; font-family: "Open Sans", sans-serif; color: var(--ink); }

  .cv-page { width: 900px; height: 675px; background: var(--paper); display: flex; flex-direction: column; }
  .cv-main { display: flex; height: 420px; }

  .profile { width: 330px; background: var(--side); padding: 18px 26px 0 40px; }
  .experience { flex: 1; padding: 0 40px 0 32px; }

  .section-title { display: flex; align-items: center; gap: 14px; margin-bottom: 12px; }
  .section-icon { width: 36px; height: 36px; background: var(--teal); display: flex; align-items: center; justify-content: center; }
  .section-icon.plain { background: none; }
  .section-title h2 { font-family: "Oswald", sans-serif; font-weight: 500; font-size: 25px; color: var(--teal); letter-spacing: .5px; text-transform: uppercase; }

  .profile p { font-size: 12.6px; line-height: 1.5; font-weight: 300; text-align: justify; }

  .skill-table { width: 100%; border-collapse: collapse; font-size: 11px; margin-bottom: 28px; }
  .skill-table th { background: var(--teal-dark); color: #fff; font-weight: 400; text-align: left; padding: 0 10px; width: 170px; height: 22px; white-space: nowrap; font-size: 10.5px; }
  .skill-table td { border-left: 2px solid #fff; padding: 0 8px; }
  .skill-table tr:nth-child(odd) td { background: var(--table-light); }
  .skill-table tr:nth-child(even) td { background: var(--table-pale); }

  .experience > p { font-size: 12.2px; line-height: 1.5; margin-bottom: 8px; }
  .experience ul { list-style: none; }
  .experience li { position: relative; padding-left: 30px; font-size: 12.2px; line-height: 1.5; margin-bottom: 4px; }
  .experience li svg { position: absolute; left: 4px; top: 5px; }

  .skills { height: 200px; background: var(--skills-band); padding: 22px 50px 0; }
  .skills-title { display: flex; justify-content: center; align-items: center; gap: 18px; margin-bottom: 18px; }
  .skills-title h2 { font-family: "Oswald", sans-serif; font-weight: 500; font-size: 25px; color: #fff; letter-spacing: 1px; }
  .skill-grid { display: grid; grid-template-columns: repeat(5, 1fr); gap: 18px 22px; }
  .skill { border: 2px solid var(--skill-line); height: 40px; display: flex; align-items: center; justify-content: center; font-family: "Oswald", sans-serif; font-size: 17px; color: #fff; white-space: nowrap; }

  .footer { flex: 1; background: var(--footer); color: #fff; font-family: "Oswald", sans-serif; font-size: 14px; letter-spacing: 1px; text-align: center; display: flex; flex-direction: column; justify-content: center; line-height: 1.45; text-transform: uppercase; }
</style>
</head>
<body>
<main class="cv-page">
  <div class="cv-main">
    <section class="profile">
      <div class="section-title">
        <span class="section-icon">
          <svg width="22" height="18" viewBox="0 0 22 18" fill="#fff"><circle cx="6" cy="5" r="3"/><circle cx="16" cy="5" r="3"/><path d="M1 16c0-4 2-6 5-6s5 2 5 6zM11 16c0-4 2-6 5-6s5 2 5 6z"/></svg>
        </span>
        <h2>Profilbeskrivelse</h2>
      </div>
      <p>Erfaren software udvikler med 25 års erfaring, som selvstændig hvor han bl.a. har arbejdet med udvikling af kundespecifikke applikationer til VinduOS til WEB i samarbejde med kunder/brugere. Derudover stor erfaring med analyse, design, programmering, test, uddannelse/undervisning, kundesupport og projektledelse. Ud over at være en dygtig software udvikler er han også en stabil og rutineret konsulent, som er vant til at yde konsulentbistand, support og udvikling af softwareløsninger til VinduOS, FjordOS og WEB.</p>
    </section>

    <section class="experience">
      <table class="skill-table">
        <tr><th>Programmeringssprog</th><td>Pelikan</td><td></td><td></td><td></td></tr>
        <tr><th>Projektledelse</th><td></td><td></td><td></td><td></td></tr>
        <tr><th>System drift/Administration</th><td></td><td></td><td></td><td></td></tr>
        <tr><th>Webservice</th><td></td><td></td><td></td><td></td></tr>
        <tr><th></th><td></td><td></td><td></td><td></td></tr>
      </table>

      <div class="section-title">
        <span class="section-icon plain">
          <svg width="30" height="24" viewBox="0 0 30 24" fill="var(--teal)"><rect x="0" y="2" width="4" height="3"/><rect x="8" y="2" width="22" height="3"/><rect x="0" y="10" width="4" height="3"/><rect x="8" y="10" width="22" height="3"/><rect x="0" y="18" width="4" height="3"/><rect x="8" y="18" width="22" height="3"/></svg>
        </span>
        <h2>Erhvervs erfaringer</h2>
      </div>
      <p>Været selvstændig i 25 år med egen virksomhed hvor forretningsområdet primært bestod i udvikling af kundespecifikke applikationer til VinduOS, FjordOS og WEB primært baseret på Visual Grund, Aspen, Kaffa, Pelikan, NordSQL, MinSQL, Orakel DB, DataDør, Paradigma DB.</p>
      <ul>
        <li><svg width="12" height="10" viewBox="0 0 12 10"><path d="M1 5l3 3 7-7" fill="none" stroke="#333" stroke-width="1.6"/></svg>WEB-baseret pakkelistesystem til Nordhavn Maskiner med mulighed for leverandørregistreringer og opfølgning (shipping/expediting) hos Nordhavn Maskiner. Tilsvarende system udviklet til Vestkyst Katalyse.</li>
        <li><svg width="12" height="10" viewBox="0 0 12 10"><path d="M1 5l3 3 7-7" fill="none" stroke="#333" stroke-width="1.6"/></svg>Kørselsregistreringssystem udviklet i Visual Grund som VinduOS-applikation til Statens Logistik.</li>
        <li><svg width="12" height="10" viewBox="0 0 12 10"><path d="M1 5l3 3 7-7" fill="none" stroke="#333" stroke-width="1.6"/></svg>Beregnings- og administrationsprogrammer til De Danske Hobbyforeninger (i dag også anvendt i Sverige og Norge), dels som VinduOS-applikationer, dels WEB på FjordOS-server.</li>
      </ul>
    </section>
  </div>

  <section class="skills">
    <div class="skills-title">
      <svg width="20" height="24" viewBox="0 0 20 24" fill="none" stroke="#fff" stroke-width="1.8"><rect x="2" y="4" width="16" height="18" rx="1"/><rect x="6" y="1" width="8" height="5" fill="var(--skills-band)"/><path d="M6 13l3 3 5-6"/></svg>
      <h2>SKILLS</h2>
    </div>
    <div class="skill-grid">
      <div class="skill">Kvadra</div>
      <div class="skill">Visual Grund</div>
      <div class="skill">Kaffa</div>
      <div class="skill">VGScript</div>
      <div class="skill">Pelikan</div>
      <div class="skill">Aspen</div>
      <div class="skill">NordSQL</div>
      <div class="skill">K ++</div>
      <div class="skill">DataDør</div>
      <div class="skill">MinSQL</div>
    </div>
  </section>

  <footer class="footer">
    <span>Solbakken Data ApS - Skovbrynet 12 - 2100 København Ø - Denmark</span>
    <span>+45 3100 4400 - info@solbakken-data.dk</span>
  </footer>
</main>
</body>
</html>
```